Business Consulting Website Design

UPDATED KEY MESSAGES:

The client has decided o a different direction.

The Key Messages include:
-- Creating something unique.
Every company is unique, ever culture unique. Every project customized to meet the unique needs of the client. No two things are alike.
-- One of a kind
Because every company is different, every culture is different, every objective is unique
-- Customized solutions
We create something just for you …

I think the approach needs to be about creating a masterpiece as opposed to nurturing/growing.

Perhaps we could have different abstract/colorful paint items that takes up part of the page for each landing page. Against white and on the white is where we put our text.

Client also has created a Pixelgrove Lightbox with images that she likes

http://www.pixelgrove-example.com/public_board.mhtml?code=a7c2e9f04b8d13562e7f90a1c4d6b852&board_id=58217409

She also likes the watercolor look against white background.

===============================
Need a Homepage and an Interior page redesign for my client: http://www.brightwavecounsel-example.com

Client does leadership development, performance management, talent development, etc. Has some great clients.

- This site is very old and needs a modern look. Update look & colors. She wants simple but not bland.
- Banner images should be interesting.
- She likes the purple in her logo
- She thinks Arial font is outdated and boring
- We will be rewriting all the copy.
- Design should include ProLinker icon, phone, email, and address
- She likes the client grid on the Our Clients page. We will be redoing this.

- Menus will include:
-- Home
-- What We Do
-- Who We Are
-- Our Clients
-- Snapshots (these are case studies)

One of the sites she liked is http://lanternfold-novel-example.com, though this website has much more content than she will have.

I'm attaching the following files for your reference:
- Her new business card proof that contains her logo
- a zip file containing some stock image comps

Need strong design. Site will likely be built in Wordpress.

Thanks,
Nora
Updates

Target Market(s)

SVP of Human Resources or Head of Talent

Industry/Entity Type

Business

Number of Pages Required

2 page

Font styles to use
Sans Serif

Colors
b768aa
876aae
6b449b
f04a50
f37122

Requirements
Must have
• - Designer must read the brief
• - Use logo
Nice to have
• - Strong banner images to complement the key message
• - Design will function work on mobile easily
Should not have
• - Should not look like a design template was purchased from layoutbazaar-example.com or other template sites.
• - Should not be too masculine
• - Should not feel cluttered.

```html
<!DOCTYPE html>
<html lang="en">
<head>
<meta charset="utf-8">
<title>Brightwave Counsel — Home</title>
<link href="https://fonts.googleapis.com/css2?family=Raleway:wght@400;500;600;700&display=swap" rel="stylesheet">
<style>
  :root {
    --page-bg: #f8f8f8;
    --purple: #4b2475;
    --purple-soft: #6b449b;
    --teal: #1f8580;
    --nav-text: #5d5d5d;
    --rule: #e4e4e4;
    --footer-text: #9a9a9a;
    --copy-text: #555555;
    --social: #2a8fc9;
  }
  * { box-sizing: border-box; margin: 0; padding: 0; }
  html, body { width: 1200px; height: 654px; overflow: hidden; }
  body {
    background: var(--page-bg);
    font-family: "Raleway", sans-serif;
    position: relative;
  }
  .site-header {
    position: absolute; left: 86px; top: 0; width: 1028px; height: 142px;
    border-bottom: 1px solid var(--rule);
  }
  .social-links {
    position: absolute; left: 0; top: 62px;
    display: flex; gap: 14px;
    font-size: 11px; font-weight: 600; color: var(--social);
  }
  .brand {
    position: absolute; left: 50%; top: 30px; transform: translateX(-50%);
    display: flex; flex-direction: column; align-items: center; gap: 8px;
    color: var(--purple); font-weight: 500; text-align: center;
  }
  .brand-mark { width: 18px; height: 18px; background: var(--purple-soft); }
  .brand-name { font-size: 17px; letter-spacing: 5px; line-height: 22px; }
  .search-icon { position: absolute; right: 0; top: 62px; }
  .main-nav {
    position: absolute; left: 0; top: 142px; width: 1200px; height: 54px;
    display: flex; justify-content: center; align-items: center; gap: 35px;
    font-size: 13.5px; color: var(--nav-text); text-transform: uppercase;
  }
  .main-nav .current { color: var(--purple); font-weight: 700; }
  .hero {
    position: absolute; left: 86px; top: 196px; width: 1028px; height: 281px;
    background:
      radial-gradient(ellipse at 18% 35%, #d01a3a 0%, rgba(208,26,58,0) 32%),
      radial-gradient(ellipse at 55% 70%, #f27fb3 0%, rgba(242,127,179,0) 40%),
      radial-gradient(ellipse at 72% 20%, #c9a21c 0%, rgba(201,162,28,0) 25%),
      radial-gradient(ellipse at 90% 40%, #d9933a 0%, rgba(217,147,58,0) 25%),
      radial-gradient(ellipse at 8% 85%, #4e8fd0 0%, rgba(78,143,208,0) 25%),
      linear-gradient(120deg, #eef0ea, #f7d6e6);
  }
  .hero-band {
    position: absolute; left: 0; top: 114px; width: 100%; height: 64px;
    background: rgba(255,255,255,0.62);
    text-align: center;
  }
  .hero-kicker { margin-top: 6px; font-size: 19px; color: var(--teal); font-weight: 500; }
  .hero-title {
    margin-top: 4px; font-size: 27px; font-weight: 700;
    letter-spacing: 4px; color: var(--purple);
  }
  .site-footer {
    position: absolute; left: 0; top: 521px; width: 1200px; text-align: center;
  }
  .contact { font-size: 10.5px; color: var(--footer-text); line-height: 16px; }
  .contact .sep { margin: 0 9px; }
  .footer-social {
    margin-top: 12px; display: flex; justify-content: center; gap: 16px;
    font-size: 10px; font-weight: 600; color: #a8a8a8;
  }
  .copyright { margin-top: 12px; font-size: 10.5px; color: var(--copy-text); }
</style>
</head>
<body>
  <header class="site-header">
    <nav class="social-links" aria-label="Social profiles">
      <span>Chirper</span><span>Friendbook</span><span>ProLinker</span>
    </nav>
    <div class="brand">
      <span class="brand-mark"></span>
      <span class="brand-name">BRIGHTWAVE<br>COUNSEL</span>
    </div>
    <svg class="search-icon" width="20" height="20" viewBox="0 0 20 20" aria-label="Search">
      <circle cx="8" cy="8" r="6.5" fill="none" stroke="#6b449b" stroke-width="1.4"/>
      <line x1="12.8" y1="12.8" x2="18.5" y2="18.5" stroke="#6b449b" stroke-width="1.4"/>
    </svg>
  </header>

  <nav class="main-nav" aria-label="Main">
    <span class="current">Home</span>
    <span>What We Do</span>
    <span>Who We Are</span>
    <span>Our Clients</span>
    <span>Snapshots</span>
  </nav>

  <section class="hero" role="img" aria-label="Close-up of paint brushes over a palette of bright red, pink, yellow and blue paint">
    <div class="hero-band">
      <p class="hero-kicker">Designing, Developing &amp; Implementing</p>
      <h1 class="hero-title">HUMAN RESOURCE COMMUNICATIONS</h1>
    </div>
  </section>

  <footer class="site-footer">
    <p class="contact">Marion Ellsworth Tate, Principal<span class="sep">|</span>office 555.214.0386<span class="sep">|</span>218 Larkspur Lane NW<br>Riverton, Georgia 30999<span class="sep">|</span>Marion@BrightwaveCounsel-example.com</p>
    <div class="footer-social"><span>Chirper</span><span>Friendbook</span><span>ProLinker</span></div>
    <p class="copyright">© 2003-2015 Brightwave Counsel</p>
  </footer>
</body>
</html>
```